Small Catering Menu

I am looking to make a small menu for catering for my company. I am thinking of a small A5 size booklet which will also have some pictures and the cover needs to be attractive.
Likely to be 8-12 pages depending upon your design (could be less or more). I need 2-3 pages as proposal concept (Cover, inside first page and one menu page) and if we like it we will make the project guaranteed before finishing the rest of the project to add security for the designer.
Pictures will be provided to the designer whose concept is the best as they are too heavy. But use generic photos for now (rather large ones) if possible.
Logo is available and so is the inside text as well as some other tidbits.
I will provide the fonts too to ensure it maintains the corporate integrity that we are following.
Catering

```html
<!DOCTYPE html>
<html lang="en">
<head>
<meta charset="utf-8">
<title>Catering Menu Cover</title>
<link href="https://fonts.googleapis.com/css2?family=Yellowtail&display=swap" rel="stylesheet">
<style>
  :root {
    --paper: #fbfcf5;
    --paper-fleck: #eef0e6;
    --spine: #0d0d0d;
    --ink: #111111;
    --outline: #6fcf8f;
  }
  html, body {
    margin: 0;
    padding: 0;
    overflow: hidden;
  }
  .cover {
    position: relative;
    width: 933px;
    height: 1200px;
    overflow: hidden;
    background:
      radial-gradient(circle at 20% 30%, var(--paper-fleck) 0 1px, transparent 2px) 0 0 / 140px 160px,
      radial-gradient(circle at 70% 60%, var(--paper-fleck) 0 1px, transparent 2px) 0 0 / 190px 120px,
      var(--paper);
    font-family: "Yellowtail", cursive;
  }
  .cover__spine {
    position: absolute;
    left: 0;
    top: 0;
    width: 26px;
    height: 100%;
    background: var(--spine);
  }
  .cover__title {
    position: absolute;
    left: 0;
    right: 0;
    top: 420px;
    margin: 0;
    text-align: center;
    font-weight: 400;
    color: var(--ink);
    line-height: 1;
    text-shadow:
      2px 0 0 var(--outline), -2px 0 0 var(--outline),
      0 2px 0 var(--outline), 0 -2px 0 var(--outline),
      2px 2px 0 var(--outline), -2px -2px 0 var(--outline),
      2px -2px 0 var(--outline), -2px 2px 0 var(--outline),
      6px 5px 0 var(--ink);
  }
  .cover__title-small {
    display: block;
    font-size: 118px;
    margin-left: -180px;
  }
  .cover__title-large {
    display: block;
    font-size: 300px;
    margin-top: -60px;
    margin-left: 10px;
  }
  .cover__brand {
    position: absolute;
    left: 0;
    right: 0;
    top: 1010px;
    margin: 0;
    text-align: center;
    font-size: 54px;
    line-height: 1.05;
    color: var(--ink);
    font-weight: 400;
  }
</style>
</head>
<body>
  <main class="cover">
    <div class="cover__spine"></div>
    <h1 class="cover__title">
      <span class="cover__title-small">the</span>
      <span class="cover__title-large">Menu</span>
    </h1>
    <p class="cover__brand">Harbor Table<br>Catering</p>
  </main>
</body>
</html>
```